Hi! We require a design for business cards for directors and head teachers of an international daycare for children 0 - 9. We are family-owned, -operated and -oriented. We have six locations, looking to franchise. Our USPs are: 1) Flexibility 2) Quality teachers 3) International culture 4) Best nutrition We are quality teachers and professional caretakers, but with creativity and personality! Business cards should be playful (but no Comic Sans or baby hand prints), colorful (but no rainbows), and have some breathing space. It should be obvious from the business card that we're a daycare. In 2020 we'll be launching our new website based on this design: https://plomvane.io/47K2RQLWZTD The font in the new website will be Houschka (medium, demibold, bold). We will keep our current logo, included in the files here. There are also screenshots of some designs we like. Show us your best! :)

Industry/Entity Type

Childcare

Contact Information for Business Card

Lotte de Vries-Bakhuis
Communications Wizard
Poppel Hoek International Daycare
Kastanjeweg 47 B, 2316 KR Leiden
www.poppelhoek.nl
+31 647315082

Font styles to use
Serif
Sans Serif

Colors

Designer to choose colors to be used in the design.

Requirements
Must have
• Color

```html
<!DOCTYPE html>
<html lang="en">
<head>
<meta charset="utf-8">
<title>Poppel Hoek – Business Cards</title>
<link rel="stylesheet" href="https://fonts.googleapis.com/css2?family=Lato:wght@400;700;900&family=Libre+Baskerville:wght@400;700&display=swap">
<style>
  :root {
    --backdrop: #e9e4dc;
    --card: #ffffff;
    --teal: #1a86ad;
    --teal-deep: #137a9f;
    --pink: #e84a86;
    --sky: #1aa9dc;
    --crimson: #b3203f;
    --title-blue: #1f6e9c;
    --petal-pink: #f4b7bd;
    --petal-yellow: #fbefb0;
    --leaf: #d6e8d2;
  }
  * { box-sizing: border-box; margin: 0; padding: 0; }
  html, body { width: 1200px; height: 939px; overflow: hidden; }
  body {
    background: var(--backdrop);
    display: flex;
    flex-direction: column;
    align-items: center;
    justify-content: center;
    gap: 56px;
    font-family: "Lato", sans-serif;
  }
  .card {
    position: relative;
    width: 640px;
    height: 366px;
    background: var(--card);
    overflow: hidden;
    box-shadow: 0 10px 26px rgba(60, 45, 30, 0.22);
  }

  /* Front */
  .garden-artwork {
    position: absolute;
    inset: 0;
    background:
      linear-gradient(180deg, rgba(255,255,255,0) 0%, rgba(255,255,255,0) 20%, var(--petal-pink) 40%, var(--petal-yellow) 60%, var(--leaf) 85%, #e4efe2 100%);
    opacity: 0.75;
  }
  .front-brand {
    position: absolute;
    left: 50%;
    top: 52%;
    transform: translate(-50%, -50%);
    display: flex;
    align-items: center;
    gap: 12px;
  }
  .brand-dot {
    width: 26px; height: 26px; border-radius: 50%;
    background: var(--pink);
  }
  .brand-name {
    font-family: "Lato", sans-serif;
    font-weight: 900;
    color: var(--pink);
    letter-spacing: 0.5px;
  }
  .front-brand .brand-name { font-size: 46px; }

  /* Back */
  .back-band { position: absolute; inset: 0; }
  .back-flowers {
    position: absolute;
    right: 40px; top: 150px;
    width: 180px; height: 130px;
    border-radius: 50%;
    background: radial-gradient(circle, rgba(120,160,200,0.55) 0%, rgba(90,150,190,0.25) 60%, rgba(26,134,173,0) 100%);
  }
  .back-brand {
    position: absolute;
    left: 54px; top: 118px;
    display: flex;
    align-items: center;
    gap: 12px;
  }
  .back-brand .brand-name { font-size: 40px; }
  .identity {
    position: absolute;
    right: 40px; top: 40px;
    text-align: right;
  }
  .person-name {
    font-family: "Libre Baskerville", serif;
    font-weight: 700;
    font-size: 22px;
    color: var(--crimson);
  }
  .person-role {
    font-family: "Libre Baskerville", serif;
    font-size: 15px;
    color: var(--title-blue);
    margin-top: 4px;
  }
  .address {
    position: absolute;
    right: 40px; top: 236px;
    text-align: right;
    color: #fff;
    font-size: 16px;
    line-height: 1.45;
  }
  .contact {
    position: absolute;
    left: 40px; bottom: 30px;
    list-style: none;
    color: #fff;
    font-size: 17px;
    line-height: 1.6;
  }
  .contact li { display: flex; align-items: center; gap: 10px; }
  .contact svg { width: 18px; height: 18px; flex: none; }
</style>
</head>
<body>

  <section class="card card-front">
    <div class="garden-artwork" role="img" aria-label="Field of soft pink and yellow flowers with green leaves and grass"></div>
    <div class="front-brand">
      <span class="brand-dot"></span>
      <span class="brand-name">Poppel Hoek</span>
    </div>
  </section>

  <section class="card card-back">
    <svg class="back-band" viewBox="0 0 640 366" preserveAspectRatio="none" aria-hidden="true">
      <polygon points="0,240 640,130 640,366 0,366" fill="var(--teal)"/>
    </svg>
    <div class="back-flowers" role="img" aria-label="Faint decorative flowers"></div>

    <div class="back-brand">
      <span class="brand-dot"></span>
      <span class="brand-name">Poppel Hoek</span>
    </div>

    <div class="identity">
      <p class="person-name">Lotte de Vries-Bakhuis</p>
      <p class="person-role">Communications Wizard</p>
    </div>

    <address class="address">
      Poppel Hoek International Daycare<br>
      Kastanjeweg 47 B, 2316 KR Leiden
    </address>

    <ul class="contact">
      <li>
        <svg viewBox="0 0 20 20" aria-hidden="true">
          <circle cx="10" cy="10" r="10" fill="var(--pink)"/>
          <path d="M7 5.5l2 2-1 1.3c.7 1.4 1.8 2.5 3.2 3.2l1.3-1 2 2-1.3 1.5C9.8 14 6 10.2 5.5 6.8z" fill="#fff"/>
        </svg>
        +31 647315082
      </li>
      <li>
        <svg viewBox="0 0 20 20" aria-hidden="true">
          <circle cx="10" cy="10" r="10" fill="var(--pink)"/>
          <circle cx="10" cy="10" r="5.5" fill="none" stroke="#fff" stroke-width="1.3"/>
          <path d="M4.5 10h11M10 4.5c-2.4 3-2.4 8 0 11M10 4.5c2.4 3 2.4 8 0 11" fill="none" stroke="#fff" stroke-width="1.1"/>
        </svg>
        www.poppelhoek.nl
      </li>
    </ul>
  </section>

</body>
</html>
```